Up and coming Australian Systems Integrator needs a proposal template refresh

We need to update our proposal template and are looking for a fresh, modern, simple and elegant proposal template. We'd like to keep our existing logos if possible.
NovaLink is a privately owned company operating since 2006. Offices and technical staff located in Quarry Bay and Tarrowby
Sustained, profitable growth year on year
Velnet strategic partner
Velnet Advanced Enterprise Network Architecture Specialisation
Velnet Advanced Security Architecture Specialisation
Velnet Advanced Collaboration Architecture Specialisation
Velnet Advanced Unified Computing Technology Specialisation
Velnet Advanced Data Centre Architecture Specialisation (in progress)
Velnet Gold Partner – Expect 2H2018
As well as being a Velnet partner we have a well established stable of other vendors such as Brakwell, Tavrimo, Harbourtone, DPQ, Moltrane Dialogic, Zell, SkyTrover, VoLERNA Drift)
We are a top two provider of Velnet product/services in the Victorian healthcare sector.
Updates
Please feel free to use different colors and fonts as we feel the existing ones look dated.

```html
<!DOCTYPE html>
<html lang="en">
<head>
<meta charset="utf-8">
<title>NovaLink Proposal Template</title>
<link rel="stylesheet" href="https://fonts.googleapis.com/css2?family=Source+Sans+3:wght@400;600;700&display=swap">
<style>
  :root {
    --page: #ffffff;
    --navy: #1a1f4b;
    --ink: #22284f;
    --label: #3a6ea5;
    --rule: #8e9db3;
    --rule-light: #d3dae4;
    --band-start: #3fd0e6;
    --band-end: #141f8a;
    --pattern-a: #eef2f8;
    --pattern-b: #c9d4e4;
    --stage: #e0a677;
  }
  * { margin: 0; padding: 0; box-sizing: border-box; }
  html, body { width: 1200px; height: 4276px; overflow: hidden; }
  body {
    position: relative;
    background: var(--page);
    font-family: "Source Sans 3", "Segoe UI", sans-serif;
    color: var(--ink);
  }
  .page { position: absolute; left: 0; width: 1200px; background: var(--page); overflow: hidden; }
  .page--cover { top: 0; height: 1696px; }
  .page--content { top: 1696px; height: 1696px; }
  .abs { position: absolute; }

  .wordmark {
    font-weight: 700;
    color: var(--navy);
    letter-spacing: 2px;
    display: flex; align-items: center; gap: 18px;
    line-height: 1;
  }
  .wordmark__square { background: var(--label); display: inline-block; }
  .cover-mark { left: 0; width: 1200px; top: 82px; justify-content: center; font-size: 96px; }
  .cover-mark .wordmark__square { width: 60px; height: 60px; }

  .cover-title { left: 336px; top: 296px; font-size: 46px; line-height: 1.1; font-weight: 700; color: var(--navy); }
  .cover-subtitle { left: 336px; top: 352px; font-size: 40px; line-height: 1.1; color: var(--navy); }
  .cover-date { left: 336px; top: 404px; font-size: 32px; line-height: 1.1; color: var(--navy); }

  .pattern {
    background: linear-gradient(200deg, var(--pattern-a) 0%, var(--pattern-b) 55%, var(--pattern-a) 100%);
    opacity: .85;
  }
  .cover-pattern { left: 0; top: 990px; width: 1200px; height: 620px; clip-path: polygon(0 100%, 100% 0, 100% 100%); }
  .content-pattern { left: 0; top: 950px; width: 1200px; height: 660px; clip-path: polygon(0 100%, 100% 0, 100% 100%); }

  .address { left: 342px; top: 1460px; font-size: 14px; line-height: 18px; color: var(--ink); font-style: normal; }
  .address strong { font-weight: 700; }

  .band {
    height: 12px;
    background: linear-gradient(90deg, var(--band-start) 0%, var(--band-start) 40%, var(--band-end) 100%);
    box-shadow: 0 3px 4px rgba(20, 31, 138, .25);
  }
  .cover-band { left: 57px; top: 1606px; width: 1083px; }

  .confidential { left: 400px; top: 22px; font-size: 27px; line-height: 1.2; color: var(--navy); }
  .header-band { left: 252px; top: 80px; width: 890px; }
  .header-mark { left: 85px; top: 108px; font-size: 46px; }
  .header-mark .wordmark__square { width: 30px; height: 30px; }

  .section { left: 254px; width: 878px; }
  .section h2 { font-size: 28px; line-height: 1.2; font-weight: 400; color: var(--navy); margin-bottom: 8px; }
  .control-table { width: 100%; border-collapse: collapse; table-layout: fixed; }
  .control-table th {
    text-align: left; font-size: 18px; font-weight: 600; color: var(--label);
    padding: 2px 0 2px 4px; border-top: 2px solid var(--rule); border-bottom: 1px solid var(--rule);
  }
  .control-table td { height: 24px; border-bottom: 1px solid var(--rule-light); }
  .control-table tr:last-child td { border-bottom: 2px solid var(--rule); }

  .section--control { top: 234px; }
  .section--distribution { top: 468px; }
  .section--definitions { top: 704px; }

  .footer-band { left: 57px; top: 1610px; width: 1083px; }
  .footer-confidential { left: 0; width: 1200px; top: 1628px; text-align: center; font-size: 24px; line-height: 1.2; font-weight: 600; color: var(--navy); }
  .page-number { right: 74px; top: 1662px; font-size: 22px; line-height: 1.2; color: var(--navy); }

  .stage { position: absolute; left: 0; top: 3392px; width: 1200px; height: 884px; background: var(--stage); }
</style>
</head>
<body>

<section class="page page--cover">
  <div class="abs wordmark cover-mark"><span class="wordmark__square"></span>NovaLink</div>

  <h1 class="abs cover-title">Title (do not use forced returns)</h1>
  <p class="abs cover-subtitle">Subtitle (do not use returns)</p>
  <p class="abs cover-date">d mmmm yyyy</p>

  <div class="abs pattern cover-pattern" role="img" aria-label="Faint pale-blue perspective pattern of square data blocks"></div>

  <address class="abs address">
    Level 3 18 Corran Street, Quarry Bay Vic 3910<br>
    2/47 Tasker Street, Tarrowby Victoria 3661<br>
    PO Box 218, Tarrowby Victoria 3662<br>
    P: 1800 555 014<br>
    E: hello@novalink.example<br>
    <strong>www.novalink.example</strong><br>
    ABN 51 824 306 917
  </address>

  <div class="abs band cover-band"></div>
</section>

<section class="page page--content">
  <p class="abs confidential">Commercial-In Confidence</p>
  <div class="abs band header-band"></div>
  <div class="abs wordmark header-mark"><span class="wordmark__square"></span>NovaLink</div>

  <div class="abs section section--control">
    <h2>Document Control</h2>
    <table class="control-table">
      <colgroup><col style="width:9%"><col style="width:26%"><col style="width:37%"><col style="width:28%"></colgroup>
      <tr><th>Version</th><th>Author</th><th>Description</th><th>Approval</th></tr>
      <tr><td></td><td></td><td></td><td></td></tr>
      <tr><td></td><td></td><td></td><td></td></tr>
      <tr><td></td><td></td><td></td><td></td></tr>
      <tr><td></td><td></td><td></td><td></td></tr>
    </table>
  </div>

  <div class="abs section section--distribution">
    <h2>Distribution List</h2>
    <table class="control-table">
      <colgroup><col style="width:21%"><col style="width:46%"><col style="width:33%"></colgroup>
      <tr><th>Name</th><th>Company</th><th>Role</th></tr>
      <tr><td></td><td></td><td></td></tr>
      <tr><td></td><td></td><td></td></tr>
      <tr><td></td><td></td><td></td></tr>
    </table>
  </div>

  <div class="abs section section--definitions">
    <h2>Definitions</h2>
    <table class="control-table">
      <colgroup><col style="width:21%"><col style="width:79%"></colgroup>
      <tr><th>Term</th><th>Definition</th></tr>
      <tr><td></td><td></td></tr>
      <tr><td></td><td></td></tr>
      <tr><td></td><td></td></tr>
    </table>
  </div>

  <div class="abs pattern content-pattern" role="img" aria-label="Faint pale-blue perspective pattern of square data blocks"></div>

  <div class="abs band footer-band"></div>
  <p class="abs footer-confidential">Commercial-in-Confidence</p>
  <p class="abs page-number">Page 2 of 4</p>
</section>

<div class="stage"></div>

</body>
</html>
```